Modern brochure by Lawyers, for modern clients

It'sa "News" for their clients. Attached you can find the current News without design. It must be elegant but very attractive and modern. Their web site is http://www.montalbanyasociados.cl/ Their expertise is labor and employment practice area. It must be in editable format so that lawyers can write the news in a template with this corporate design.

Target Market(s)

Big Companies

Font styles to use
Sans Serif

Colors
0255a3
474747

Requirements
Nice to have
• Legal Pictures and only a little of yellow. One touch! It must be in editable format so that lawyers can write the news in a template with this corporate design.

```html
<!DOCTYPE html>
<html lang="es">
<head>
<meta charset="utf-8">
<title>Montalbán y Asociados Abogados — Noticias</title>
<link rel="stylesheet" href="https://fonts.googleapis.com/css2?family=Didact+Gothic&display=swap">
<style>
  :root {
    --stage: #5f6672;
    --paper: #ffffff;
    --navy: #3e5470;
    --slate: #8a9aa6;
    --mist: #c2ced6;
    --frost: #e4eaee;
    --ink: #2c2c2c;
  }
  * { margin: 0; padding: 0; box-sizing: border-box; }
  html, body { width: 1200px; height: 1200px; overflow: hidden; background: var(--stage); }
  .newsletter {
    position: absolute; left: 294px; top: 201px;
    width: 593px; height: 816px;
    background: var(--paper);
    font-family: "Didact Gothic", "Century Gothic", sans-serif;
    color: var(--ink);
  }
  .brand-name {
    position: absolute; left: 84px; top: 78px; width: 428px;
    font-family: "Didact Gothic", "Century Gothic", sans-serif;
    font-weight: 400; font-size: 26px; line-height: 34px;
    letter-spacing: 2px; color: var(--navy); white-space: nowrap;
  }
  .brand-name span { display: block; }
  .hero {
    position: absolute; left: 0; top: 176px; width: 593px; height: 100px;
    background: linear-gradient(180deg, #3f4f66 0%, #7d7a78 45%, #4d5a6e 75%, #34425a 100%);
  }
  .date {
    position: absolute; right: 84px; top: 295px;
    font-size: 12px;
  }
  .date-rule { position: absolute; left: 251px; top: 322px; }
  .body {
    position: absolute; left: 84px; top: 339px; width: 428px;
    font-size: 11.6px; line-height: 14.4px;
  }
  .body p { margin-bottom: 14.4px; }
  .body a { color: inherit; text-decoration: none; }
  .footer-bands { position: absolute; left: 0; bottom: 0; }
</style>
</head>
<body>
  <article class="newsletter">
    <h1 class="brand-name">
      <span>MONTALBÁN Y ASOCIADOS</span>
      <span>ABOGADOS</span>
    </h1>

    <div class="hero" role="img" aria-label="Fotografía de unos anteojos sobre un escritorio frente a una biblioteca de libros jurídicos"></div>

    <p class="date">Santiago, 25 de julio de 2018</p>
    <svg class="date-rule" width="259" height="3" viewBox="0 0 259 3">
      <rect x="0" width="64" height="3" fill="var(--frost)"/>
      <rect x="65" width="64" height="3" fill="var(--mist)"/>
      <rect x="130" width="64" height="3" fill="var(--slate)"/>
      <rect x="195" width="64" height="3" fill="var(--navy)"/>
    </svg>

    <section class="body">
      <p>Estimados,</p>
      <p>Por medio del presente, les damos a conocer el Dictamen Ordinario N° 3826-031, emitido por la Inspección Nacional Laboral el pasado 20 de julio, relativo a los “beneficios históricos”.</p>
      <p>Estos fueron definidos en su oportunidad por este organismo como “…aquellos beneficios que se han otorgado desde siempre…” por parte del empleador.</p>
      <p>A partir de este Dictamen, el cual reconsidera el criterio del anterior Director de la Inspección, los beneficios históricos vuelven a ser patrimonio de la empresa y de los trabajadores que los han recibido, dejando de serlo de la organización sindical y de sus socios beneficiados por el solo hecho de haberse “replicado” en un instrumento colectivo durante una negociación.</p>
      <p>Por último, el Dictamen en comento aclara que si un “beneficio histórico” se incrementa de manera real y efectiva producto de una negociación colectiva, únicamente dicho incremento se entenderá originado en el respectivo instrumento colectivo, y en consecuencia, objeto de una posible extensión en el evento de que ésta se haya acordado durante la negociación.</p>
      <p>Para mayor análisis de lo resuelto por la Inspección Nacional Laboral, se puede revisar el Dictámen en comento haciendo click <a href="http://www.montalbanyasociados.cl/">aquí</a></p>
      <p>Sin otro particular, saluda atentamente a ustedes,</p>
      <p>Montalbán y Asociados Abogados<br>oficina@montalbanyasociados.cl</p>
    </section>

    <svg class="footer-bands" width="593" height="18" viewBox="0 0 593 18">
      <rect x="0" width="152" height="18" fill="var(--navy)"/>
      <rect x="152" width="147" height="18" fill="var(--slate)"/>
      <rect x="299" width="147" height="18" fill="var(--mist)"/>
      <rect x="446" width="147" height="18" fill="var(--frost)"/>
    </svg>
  </article>
</body>
</html>
```